Graphic Design/Logo Needed for Ear Drops Bottle

We have an Ear Drop Medication that we need to create a new label for. We will use a retro picture of a Doctor (Dr. Blenham) and the name of the product is Tidy Lobe. There is no official logo, so we will want to create a retro, basic logo for Tidy Lobe and use the retro picture. Front portion of the label is Size is 1.5" in height, and about 1.375" Width. this is a small tube similar in size to eye drops. We will be looking for just the logo portion and what you will see on the front of the bottle.

Target Market(s)

Medical Container

Industry/Entity Type

Medical

Font styles to use
Serif
Sans Serif

Colors
0054AA
0677BA
7BADD7
CADEEF
E8F1F8
FFF300
FFF600
FEFA6F
FFFEC7
FFFEE8

Requirements
Must have
• Picture of Dr. Blenham, "Tidy Lobe", Dr. Blenham's Ear Solution
Nice to have
• Retro Style or Modern with Retro Feel, Clean and engaging

```html
<!DOCTYPE html>
<html lang="en">
<head>
<meta charset="utf-8">
<title>Tidy Lobe – Dr. Blenham's Ear Solution label</title>
<link rel="stylesheet" href="https://fonts.googleapis.com/css2?family=Libre+Baskerville:wght@400;700&display=swap">
<style>
  :root {
    --page-bg: #cfcfcf;
    --yellow: #e6db3e;
    --navy: #2f4a8a;
    --blue-deep: #3d5494;
    --blue-mid: #4f7fb5;
    --blue-pale: #9fd3e0;
    --white: #ffffff;
    --portrait-tone: #c9d2e4;
  }
  * { box-sizing: border-box; margin: 0; padding: 0; }
  html, body {
    width: 1200px;
    height: 750px;
    overflow: hidden;
    background: var(--page-bg);
  }
  .canvas {
    position: relative;
    width: 1200px;
    height: 750px;
  }
  .label {
    position: absolute;
    left: 335px;
    top: 86px;
    width: 529px;
    height: 578px;
    overflow: hidden;
    font-family: "Libre Baskerville", Georgia, serif;
  }
  .label__backdrop {
    position: absolute;
    inset: 0;
    background: linear-gradient(90deg,
      var(--blue-pale) 0%,
      var(--blue-mid) 22%,
      var(--blue-deep) 40%,
      var(--blue-deep) 60%,
      var(--blue-mid) 78%,
      var(--blue-pale) 100%);
  }
  .label__band-top {
    position: absolute;
    left: 0; top: 0;
    width: 100%; height: 13px;
    background: var(--yellow);
  }
  .label__band-bottom {
    position: absolute;
    left: 0; bottom: 0;
    width: 100%; height: 32px;
    background: var(--yellow);
    border-top: 4px solid var(--blue-pale);
  }
  .label__band-line {
    position: absolute;
    left: 0; bottom: 40px;
    width: 100%; height: 3px;
    background: var(--yellow);
  }
  .badge {
    position: absolute;
    left: 90px;
    top: 81px;
    width: 348px;
    height: 218px;
    border-radius: 50%;
    background: var(--white);
    border: 2px solid var(--white);
    box-shadow: inset 0 0 0 3px var(--white), inset 0 0 0 4.5px var(--navy);
  }
  .badge__portrait {
    position: absolute;
    left: 124px;
    top: 16px;
    width: 100px;
    height: 94px;
    border-radius: 40% 40% 8% 8%;
    background: linear-gradient(180deg, var(--portrait-tone), #e9edf5);
  }
  .badge__name {
    position: absolute;
    left: 0; right: 0;
    top: 114px;
    text-align: center;
    color: var(--navy);
    font-size: 40px;
    font-weight: 700;
    line-height: 1;
    letter-spacing: -0.5px;
  }
  .badge__maker {
    position: absolute;
    left: 0; right: 0;
    top: 157px;
    text-align: center;
    color: var(--navy);
    font-size: 19px;
    font-weight: 700;
    line-height: 1;
  }
  .product-type {
    position: absolute;
    left: 156px;
    top: 348px;
    width: 217px;
    height: 42px;
    border-radius: 21px;
    background: var(--yellow);
    border: 3px solid var(--white);
    display: flex;
    align-items: center;
    justify-content: center;
    color: #4a5fa0;
    font-size: 15px;
    letter-spacing: 2.5px;
  }
  .volume {
    position: absolute;
    left: 0; right: 0;
    top: 513px;
    text-align: center;
    color: var(--white);
    font-size: 16px;
    font-weight: 700;
  }
</style>
</head>
<body>
<main class="canvas">
  <section class="label" aria-label="Tidy Lobe ear drops front label">
    <div class="label__backdrop" role="img" aria-label="Decorative flowing blue background pattern"></div>
    <div class="label__band-top"></div>

    <div class="badge">
      <div class="badge__portrait" role="img" aria-label="Retro portrait of Dr. Blenham"></div>
      <p class="badge__name">Tidy Lobe</p>
      <p class="badge__maker">Dr. Blenham's</p>
    </div>

    <p class="product-type">EAR SOLUTION</p>
    <p class="volume">5ml</p>

    <div class="label__band-line"></div>
    <div class="label__band-bottom"></div>
  </section>
</main>
</body>
</html>
```